Website for "Bright Meadow Ltd" cleaning bsuiness

We require a website to expose our business to the local market. We want to provide background on who we are and what we do but in an easily digestible way. We clean domestic and commercial premises and want to provide a list of all of our services to potential customers. We operate out of Warrington in the UK.

We would like the website to be animated in some way so that the experience of using it is not dull or mundane. This website needs to be an extension of our company.

Target Market(s)

30 - 60 year olds for Domestic plus commercial clients

Industry/Entity Type

Cleaning Service

Coding

Coded - Design and coding required

Number of Pages Required

4 page

Font styles to use
Sans Serif

Colors
0455a3
3176b5
85acd3
cfdeed
ffffff
000000
1b1b1b
c8c8c8
757575

Requirements
Must have
• Logo which has been provided. Theme based around the logo and its colours. Simple layout to avoid confusion.
Nice to have
• Animations where possible to impress the customer.
Should not have
• any pictures of cleaning equipment, fairies, maids etc

```html
<!DOCTYPE html>
<html lang="en">
<head>
<meta charset="utf-8">
<title>Bright Meadow Ltd – Professional Cleaning</title>
<link href="https://fonts.googleapis.com/css2?family=Oswald:wght@300;400;500&family=Open+Sans:wght@400;600&display=swap" rel="stylesheet">
<style>
:root{
  --brand-deep:#0455a3;
  --brand:#3176b5;
  --brand-bright:#2f78e0;
  --brand-soft:#85acd3;
  --brand-pale:#cfdeed;
  --white:#ffffff;
  --black:#000000;
  --ink:#1b1b1b;
  --line:#c8c8c8;
  --muted:#757575;
  --footer:#3b3b3b;
}
*{box-sizing:border-box;margin:0;padding:0}
html,body{width:1200px;height:2406px;overflow:hidden;background:var(--white)}
body{font-family:"Open Sans",Verdana,sans-serif;color:var(--ink);position:relative}
.heading{font-family:"Oswald",sans-serif;font-weight:400}
a{color:inherit;text-decoration:none}

/* header */
.site-header{position:absolute;top:0;left:0;width:1200px;height:77px;background:var(--white)}
.brand{position:absolute;left:230px;top:18px;display:flex;align-items:center;gap:8px;font-family:"Oswald",sans-serif;font-size:22px;color:var(--brand-deep)}
.brand-dot{width:14px;height:14px;border-radius:50%;background:var(--brand-deep)}
.header-phone{position:absolute;left:885px;top:15px;display:flex;align-items:center;gap:8px;font-size:12px;color:var(--ink)}
.main-nav{position:absolute;top:46px;left:521px;display:flex;gap:0;font-family:"Oswald",sans-serif;font-size:16px;color:var(--brand-deep)}
.main-nav a{position:absolute;white-space:nowrap}

/* hero */
.hero{position:absolute;top:77px;left:0;width:1200px;height:438px;background:linear-gradient(180deg,#2a3a4c 0%,#3d4a57 45%,#2b2f34 100%)}
.hero-title{position:absolute;left:230px;top:120px;font-family:"Oswald",sans-serif;font-weight:500;font-size:66px;line-height:76px;color:var(--white)}
.hero-call{position:absolute;right:230px;top:310px;text-align:right;font-family:"Oswald",sans-serif;font-weight:300;color:var(--white);font-size:24px;line-height:37px}
.hero-call strong{font-weight:500;font-size:27px}

/* about */
.about{position:absolute;top:515px;left:0;width:1200px;height:310px}
.about-title{position:absolute;left:208px;top:60px;font-size:25px;color:var(--brand-deep)}
.about-text{position:absolute;left:208px;top:98px;width:372px;font-size:13px;line-height:19px}
.more{font-size:9px;color:var(--ink)}
.about .more{position:absolute;left:527px;top:245px}
.video{position:absolute;left:624px;top:59px;width:348px;height:194px;background:linear-gradient(135deg,#4a4e4c,#2e3230 60%,#5a5f5a);display:flex;flex-direction:column;align-items:center;justify-content:center;color:var(--white);font-size:14px;gap:4px}

/* services */
.services{position:absolute;top:825px;left:0;width:1200px;height:691px;background:linear-gradient(180deg,#3a3b3d 0%,#2d2a28 60%,#3a352e 100%)}
.services-title{position:absolute;top:26px;width:1200px;text-align:center;font-size:25px;color:var(--white)}
.service-card{position:absolute;width:350px;height:171px;background:rgba(47,120,224,.82);color:var(--white);padding:14px 20px 0}
.service-card h3{font-family:"Oswald",sans-serif;font-weight:400;font-size:19px;text-align:center;text-decoration:underline;margin-bottom:10px}
.service-card p{font-size:11px;line-height:15px}
.service-card .more{position:absolute;right:18px;bottom:12px;color:var(--white)}

/* feedback */
.feedback{position:absolute;top:1516px;left:0;width:1200px;height:265px}
.feedback-title{position:absolute;top:46px;width:1200px;text-align:center;font-size:25px;color:var(--brand-bright)}
.feedback-quote{position:absolute;left:275px;top:95px;width:650px;text-align:center;font-size:13px;line-height:20px}
.feedback-name{position:absolute;top:188px;width:1200px;text-align:center;font-size:13px;font-weight:600}
.arrow{position:absolute;top:118px}

/* contact */
.contact{position:absolute;top:1781px;left:0;width:1200px;height:372px;background:linear-gradient(180deg,#2e2c2a,#3a3631 55%,#23211f)}
.contact-title{position:absolute;top:44px;width:1200px;text-align:center;font-size:25px;color:var(--white)}
.contact-info{position:absolute;left:237px;top:114px;font-family:"Oswald",sans-serif;color:var(--white);font-size:17px;line-height:37px}
.contact-info .address{font-size:15px;line-height:20px;margin-top:4px}
.contact-form{position:absolute;left:637px;top:102px;width:300px}
.field{height:47px;border-bottom:1px solid var(--line);color:var(--line);font-size:14px;padding:10px 0 0 16px}
.send{position:absolute;left:70px;top:197px;width:174px;height:28px;border-radius:14px;background:var(--brand-bright);color:var(--white);font-size:12px;text-align:center;line-height:28px}

/* social */
.follow{position:absolute;top:2153px;left:0;width:1200px;height:156px;background:var(--brand-bright)}
.follow-title{position:absolute;top:28px;width:1200px;text-align:center;font-size:25px;color:var(--white)}
.social-list{position:absolute;top:82px;left:470px;display:flex;gap:14px}
.social-list span{width:32px;height:32px;background:var(--brand-deep)}

/* footer */
.site-footer{position:absolute;top:2309px;left:0;width:1200px;height:97px;background:var(--footer);color:var(--line);text-align:center;font-family:"Oswald",sans-serif}
.footer-title{position:absolute;top:14px;width:1200px;font-size:16px;font-weight:300}
.footer-links{position:absolute;top:45px;width:1200px;font-size:13px;font-weight:300;word-spacing:0}
.footer-links a{margin:0 21px}
.copyright{position:absolute;top:76px;width:1200px;font-family:"Open Sans",sans-serif;font-size:8px}
</style>
</head>
<body>

<header class="site-header">
  <a class="brand" href="#"><span class="brand-dot"></span>Bright Meadow Ltd</a>
  <div class="header-phone">
    <svg width="14" height="14" viewBox="0 0 24 24"><path d="M6.6 10.8a15 15 0 0 0 6.6 6.6l2.2-2.2c.3-.3.7-.4 1-.2 1.1.4 2.3.6 3.6.6.6 0 1 .4 1 1V20c0 .6-.4 1-1 1A17 17 0 0 1 3 4c0-.6.4-1 1-1h3.5c.6 0 1 .4 1 1 0 1.3.2 2.5.6 3.6.1.3 0 .7-.2 1z" fill="none" stroke="#1b1b1b" stroke-width="1.6"/></svg>
    0800 123 4567
  </div>
  <nav class="main-nav">
    <a href="#" style="left:0">Who we are</a>
    <a href="#" style="left:113px">What we offer</a>
    <a href="#" style="left:239px">Franchisees</a>
    <a href="#" style="left:349px">Blog</a>
    <a href="#" style="left:422px">Contact</a>
  </nav>
</header>

<section class="hero" role="img" aria-label="Open-plan office interior with desks and large windows, dimmed">
  <h1 class="hero-title">We clean domestic<br>and commercial premises</h1>
  <p class="hero-call">CALL US ON<br><strong>0800 123 4567</strong><br>TO GET BEST SERVICE.</p>
</section>

<section class="about">
  <h2 class="about-title heading">Who are we</h2>
  <p class="about-text">Lorem Ipsum is simply dummy text of the printing and typesetting industry. Lorem Ipsum has been the industry's standard dummy text ever since the 1500s, when an unknown printer took a galley of type and scrambled it to make a type specimen book. It has survived not only five centuries, but also the leap into electronic typesetting, remaining essentially unchanged.</p>
  <a class="more" href="#">More....</a>
  <div class="video" role="img" aria-label="Video still of a bright office lobby with plants">
    <svg width="40" height="40" viewBox="0 0 40 40"><circle cx="20" cy="20" r="18" fill="none" stroke="#fff" stroke-width="1.6"/><path d="M16 12l11 8-11 8z" fill="none" stroke="#fff" stroke-width="1.6"/></svg>
    <span>Watch Video</span>
  </div>
</section>

<section class="services" role="img" aria-label="Living room with city view through tall windows, dimmed">
  <h2 class="services-title heading">What we offer</h2>
  <article class="service-card" style="left:237px;top:89px"><h3>House Cleaning</h3><p>Lorem Ipsum is simply dummy text of the printing and typesetting industry. Lorem Ipsum has been the industry's standard dummy text ever since the 1500s, when an unknown printer took a galley of type and scrambled it to make a type specimen book.</p><a class="more" href="#">More....</a></article>
  <article class="service-card" style="left:612px;top:89px"><h3>Apartment Cleaning</h3><p>Lorem Ipsum is simply dummy text of the printing and typesetting industry. Lorem Ipsum has been the industry's standard dummy text ever since the 1500s, when an unknown printer took a galley of type and scrambled it to make a type specimen book.</p><a class="more" href="#">More....</a></article>
  <article class="service-card" style="left:237px;top:285px"><h3>Commercial Cleaning</h3><p>Lorem Ipsum is simply dummy text of the printing and typesetting industry. Lorem Ipsum has been the industry's standard dummy text ever since the 1500s, when an unknown printer took a galley of type and scrambled it to make a type specimen book.</p><a class="more" href="#">More....</a></article>
  <article class="service-card" style="left:612px;top:285px"><h3>Move In/Move Out Cleaning</h3><p>Lorem Ipsum is simply dummy text of the printing and typesetting industry. Lorem Ipsum has been the industry's standard dummy text ever since the 1500s, when an unknown printer took a galley of type and scrambled it to make a type specimen book.</p><a class="more" href="#">More....</a></article>
  <article class="service-card" style="left:237px;top:482px"><h3>Green Cleaning</h3><p>Lorem Ipsum is simply dummy text of the printing and typesetting industry. Lorem Ipsum has been the industry's standard dummy text ever since the 1500s, when an unknown printer took a galley of type and scrambled it to make a type specimen book.</p><a class="more" href="#">More....</a></article>
  <article class="service-card" style="left:612px;top:482px"><h3>Office Cleaning</h3><p>Lorem Ipsum is simply dummy text of the printing and typesetting industry. Lorem Ipsum has been the industry's standard dummy text ever since the 1500s, when an unknown printer took a galley of type and scrambled it to make a type specimen book.</p><a class="more" href="#">More....</a></article>
</section>

<section class="feedback">
  <h2 class="feedback-title heading">Customers Feedback</h2>
  <svg class="arrow" style="left:226px" width="14" height="26" viewBox="0 0 14 26"><path d="M12 2L2 13l10 11" fill="none" stroke="#757575" stroke-width="1.6"/></svg>
  <p class="feedback-quote">Lorem Ipsum is simply dummy text of the printing and typesetting industry. Lorem Ipsum has been the industry's standard dummy text ever since the 1500s, when an unknown printer took a galley of type and scrambled it to make a type specimen book. It has survived not only five centuries, but also the leap into electronic typesetting, remaining essentially unchanged.</p>
  <p class="feedback-name">Harriet Lane Morrow</p>
  <svg class="arrow" style="left:958px" width="14" height="26" viewBox="0 0 14 26"><path d="M2 2l10 11L2 24" fill="none" stroke="#757575" stroke-width="1.6"/></svg>
</section>

<section class="contact" role="img" aria-label="Dim living room with bookshelves and armchair">
  <h2 class="contact-title heading">Contact Us</h2>
  <div class="contact-info">
    <p>Call Us - 0800 123 4567</p>
    <p>Email - hello@brightmeadow.example</p>
    <p class="address">Address - 27 Orchard Row WA1 2XY<br>&nbsp;&nbsp;&nbsp;&nbsp;&nbsp;&nbsp;&nbsp;&nbsp;&nbsp;&nbsp;&nbsp;&nbsp;&nbsp;&nbsp;&nbsp;&nbsp;Warrington United Kingdom.</p>
  </div>
  <form class="contact-form">
    <div class="field">User Name</div>
    <div class="field">Email ID</div>
    <div class="field">Phone Number</div>
    <div class="field">Message</div>
    <div class="send">Send</div>
  </form>
</section>

<section class="follow">
  <h2 class="follow-title heading">Follow Us On</h2>
  <div class="social-list"><span></span><span></span><span></span><span></span><span></span><span></span></div>
</section>

<footer class="site-footer">
  <p class="footer-title">QUICK LINKS</p>
  <p class="footer-links"><a href="#">Who we are</a><a href="#">What we offer</a><a href="#">Franchisees</a><a href="#">Blog</a><a href="#">Contact</a></p>
  <p class="copyright">© Bright Meadow 2015</p>
</footer>

</body>
</html>
```